Web site for small printshop

I am looking for a website for small printshop in Iceland, mainly serving university students and artist.

We print posters, flyers, business cards and more.

In addition to our current website, I would like to include design tool, (fx. www.quarvelink.com, www.tandorizo.com or something similar) jobs upload, shopping chart.
Updates

Great work, I am really amazed of the quality of work i am seeing here.

Really way beyond my expectation

GOOD JOB - all of you ! 

Hi all.

The designs submitted have been great, way better than expected.
I really did not expect this level of quality.

Some have been asking me for feedback on their designs, and I will try 
to send some feedback here, without spoiling your creativity.

Likes:
- when the colors of my logo is used in menus, buttons etc.
- simple, not to crowded look.

Dislikes.
- Dark and heavy design
- Lot of text and buttons (crowded look)

Extra info.
- top line (before menus) will contain: Tel - email - language
- menu line will have 5 categories: Home - service - submission of works - FAQ - about us
- 3 large buttons:  Job submit - Job design - ask for offer

LOVE YOUR WORK - great designs so far :)

Target Market(s)

University Students, Artists. Age group 20-30

Industry/Entity Type

University

Requirements
Must have
• The website must be easy to use, clean looking.

```html
<!DOCTYPE html>
<html lang="en">
<head>
<meta charset="utf-8">
<title>Prentvik – Printing for students and artists</title>
<link href="https://fonts.googleapis.com/css2?family=Montserrat:wght@400;600;700&family=Open+Sans:wght@400;600&display=swap" rel="stylesheet">
<style>
:root{
  --dark:#2a2a2a;
  --darker:#242424;
  --yellow:#f5d31a;
  --footer-yellow:#e3c84b;
  --red:#e8392e;
  --green-top:#3fd7a2;
  --green-bottom:#179a70;
  --green-text:#0f3a2c;
  --text:#555;
  --muted:#bdbdbd;
  --white:#fff;
}
*{margin:0;padding:0;box-sizing:border-box}
html,body{width:768px;height:1200px;overflow:hidden}
body{position:relative;background:var(--white);font-family:'Open Sans',Arial,sans-serif;color:var(--text)}
.abs{position:absolute}

.site-header{left:0;top:0;width:768px;height:66px;background:var(--dark);border-bottom:4px solid var(--yellow)}
.brand{left:90px;top:14px;display:flex;align-items:center;gap:7px;font-family:'Montserrat',sans-serif;font-weight:700;font-size:20px;color:var(--white);letter-spacing:.2px}
.brand-square{width:25px;height:33px;background:var(--red)}
.main-nav{left:369px;top:26px;display:flex;gap:11px;font-family:'Montserrat',sans-serif;font-weight:600;font-size:9px;color:var(--white)}
.main-nav .active{position:relative}
.main-nav .active::after{content:"";position:absolute;left:0;right:0;top:16px;height:2px;background:var(--yellow)}

.hero{left:0;top:66px;width:768px;height:319px;background:linear-gradient(#eeeeee,#f7f7f7)}
.hero-visual{left:90px;top:14px;width:586px;height:266px;background:linear-gradient(160deg,#fafafa 0%,#dcdcdc 55%,#bdbdbd 100%);box-shadow:0 6px 10px rgba(0,0,0,.15)}

.cta{top:412px;width:212px;height:44px;border-radius:7px;background:#dcdcdc;padding:4px}
.cta span{display:flex;align-items:center;justify-content:center;height:100%;border-radius:6px;background:linear-gradient(var(--green-top),var(--green-bottom));font-family:'Montserrat',sans-serif;font-weight:700;font-size:14.5px;color:var(--green-text);letter-spacing:.4px}
.cta-submit{left:130px}
.cta-university{left:424px}

.service{top:481px;width:140px;text-align:center}
.service-icon{display:block;margin:0 auto;width:102px;height:102px}
.service h3{margin-top:13px;font-family:'Montserrat',sans-serif;font-weight:700;font-size:13px;color:var(--red);letter-spacing:.3px}
.service h3::after{content:"";display:block;width:88px;height:3px;background:var(--red);margin:6px auto 0}
.service p{width:126px;margin:14px auto 0;font-size:9px;line-height:13.8px;color:var(--text)}
.svc-1{left:93px}.svc-2{left:240px}.svc-3{left:386px}.svc-4{left:533px}

.links-title{left:90px;top:796px;width:586px;text-align:center}
.links-title::before{content:"";position:absolute;left:0;right:0;top:9px;height:1px;background:#dcdcdc}
.links-title h2{position:relative;display:inline-block;background:var(--white);padding:0 10px;font-family:'Montserrat',sans-serif;font-weight:700;font-size:14px;letter-spacing:3px;color:#111}
.links-row{left:100px;top:836px;width:566px;display:flex;justify-content:space-between;align-items:center;font-family:'Open Sans',sans-serif;font-weight:600;font-size:19px;color:var(--muted)}

.contact{left:0;top:890px;width:768px;height:222px;background:var(--darker)}
.contact h2{position:absolute;left:0;width:768px;top:14px;text-align:center;font-family:'Montserrat',sans-serif;font-weight:700;font-size:14.5px;letter-spacing:2px;color:var(--yellow)}
.map{left:133px;top:52px;width:256px;height:152px;background:linear-gradient(135deg,#e6e6e6,#c9c9c9)}
.label{font-family:'Montserrat',sans-serif;font-weight:600;font-size:9px;letter-spacing:1.4px;color:#8a8a8a}
.info{font-size:9.5px;line-height:13.5px;color:var(--white)}
.info .hl{color:var(--yellow)}
.col-a{left:414px}.col-b{left:558px}
.social{display:flex;align-items:center;gap:6px;font-family:'Montserrat',sans-serif;font-size:9px;color:#8a8a8a}
.social i{width:21px;height:21px;border-radius:50%;background:#6a6a6a}

.site-footer{left:0;top:1112px;width:768px;height:88px;background:var(--footer-yellow);text-align:center}
.footer-mark{position:absolute;left:366px;top:12px;width:34px;height:34px;background:rgba(255,255,255,.85);display:flex;align-items:center;justify-content:center;font-family:'Montserrat',sans-serif;font-weight:700;font-size:5.5px;color:var(--footer-yellow)}
.copyright{position:absolute;left:0;width:768px;top:60px;font-size:8px;color:var(--white);letter-spacing:.3px}
</style>
</head>
<body>

<header class="site-header abs">
  <div class="brand abs"><span class="brand-square"></span>PRENTVIK</div>
  <nav class="main-nav abs">
    <span class="active">Home</span><span>Services</span><span>Submission of Works</span><span>University Printing</span><span>Contact</span>
  </nav>
</header>

<section class="hero abs">
  <div class="hero-visual abs" role="img" aria-label="Photo of printed stationery: business cards, letterhead, envelopes and a spiral desk calendar"></div>
</section>

<a class="cta cta-submit abs"><span>SUBMISSION OF WORKS</span></a>
<a class="cta cta-university abs"><span>UNIVERSITY PRINTING</span></a>

<article class="service svc-1 abs">
  <svg class="service-icon" viewBox="0 0 102 102"><circle cx="51" cy="51" r="51" fill="#e8392e"/><g transform="rotate(-10 51 51)"><rect x="27" y="30" width="48" height="40" fill="#fff"/><rect x="32" y="35" width="38" height="27" fill="#e8392e"/><path d="M34 60l12-12 8 8 5-5 10 9z" fill="#fff"/><circle cx="60" cy="42" r="3" fill="#fff"/></g></svg>
  <h3>PHOTOCOPYING</h3>
  <p>Prentvik Copy House possesses one of the most powerful equipment in Iceland for photocopying. but we provide all generic copy in color or black and white, in small or large quantities</p>
</article>

<article class="service svc-2 abs">
  <svg class="service-icon" viewBox="0 0 102 102"><circle cx="51" cy="51" r="51" fill="#e8392e"/><path d="M28 30l15 -5v47l-15 5z M45 25l13 5v47l-13-5z M60 30l15-5v47l-15 5z" fill="#fff"/></svg>
  <h3>PRINTING</h3>
  <p>We can print, brochures, invitations, business cards, newsletters, accounts or just anything you can think of. If we do not have the solution, we are in partnership with a number of companies that help us to deliver projects quickly and easily.</p>
</article>

<article class="service svc-3 abs">
  <svg class="service-icon" viewBox="0 0 102 102"><circle cx="51" cy="51" r="51" fill="#e8392e"/><rect x="31" y="27" width="40" height="50" rx="4" fill="#fff"/><rect x="71" y="34" width="4" height="7" fill="#fff"/><rect x="71" y="46" width="4" height="7" fill="#fff"/><rect x="71" y="58" width="4" height="7" fill="#fff"/><g fill="#e8392e"><circle cx="51" cy="46" r="5"/><path d="M41 62c0-7 5-10 10-10s10 3 10 10z"/></g></svg>
  <h3>BOOK PUBLISHING</h3>
  <p>We can print all kinds of books, but we have powerful equipment to print and bind the books, in quantities as desired. No quantity is too small or too big.</p>
</article>

<article class="service svc-4 abs">
  <svg class="service-icon" viewBox="0 0 102 102"><circle cx="51" cy="51" r="51" fill="#e8392e"/><rect x="29" y="29" width="46" height="46" fill="#fff"/><path d="M34 66l12-13 8 8 5-5 11 10z" fill="#e8392e"/><circle cx="63" cy="40" r="3" fill="#e8392e"/><rect x="50" y="18" width="1.5" height="66" fill="#fff"/></svg>
  <h3>SCANNING</h3>
  <p>Prentvik Studio has more than 10 years experience in the scan. We have specialized scanners and can deliver content in a way that works best, but we can scan into TIF, JPG, PDF, PDF / A, Word, Exel, txt etc.</p>
</article>

<div class="links-title abs"><h2>USEFUL LINKS</h2></div>
<div class="links-row abs">
  <span>Pagevane</span><span>Brushly</span><span>Tutorra</span><span>Openquill</span><span>Packzo</span>
</div>

<section class="contact abs">
  <h2>CONTACT</h2>
  <div class="map abs" role="img" aria-label="Street map showing the shop location in Reykjavik"></div>

  <div class="col-a abs" style="top:50px">
    <div class="label">SAY HELLO</div>
    <div class="info" style="margin-top:4px">E: <span class="hl">verk@prentvik.is</span><br>T: 555 0147</div>
  </div>
  <div class="col-a abs" style="top:120px">
    <div class="label">ADDRESS</div>
    <div class="info" style="margin-top:4px">Prentvik Copy House /<br>Prentvik Print Studio,<br>Brekkugata 9,<br>105 Reykjavik</div>
  </div>

  <div class="col-b abs" style="top:52px">
    <div class="social"><i></i>BIRDNOTE</div>
    <div class="social" style="margin-top:7px"><i></i>FRIENDWALL</div>
  </div>
  <div class="col-b abs" style="top:120px">
    <div class="label">OPENING HOURS</div>
    <div class="info" style="margin-top:4px">Mon - Fri: 9-17<br>closed on weekends</div>
  </div>
</section>

<footer class="site-footer abs">
  <div class="footer-mark">PRENTVIK</div>
  <p class="copyright">COPYRIGHT © 2013 PRENTVIK. ALL RIGHTS RESERVED.</p>
</footer>

</body>
</html>
```